small business focused on life coaching and helping others "create better tomorrows" needs a website

The Pell R Group needs a website that focuses on life coaching and helping others "create better tomorrows"; This is a sole proprietorship so the focus should be on Marla, who has worn many hats and in an excellent position to help others. It should include 6 pages _ Home, Bio, Services, Book, Media, Contact Us and the logo that was created by Craft Plaza; also include testimonials from 5-6 individuals as well as why one might need these services (see file included)

Target Market(s)

Immigrants who need help navigating American system in the workplace, home or community, immigrant or at-risk students unable to communicate with their immigrant parents (due to language or unfamiliarity with the new culture) but would share with someone they trust, those in need of a mentor or help with career advancement or choices, those in need of help with public speaking or leadership development - Marla is someone who has worn many hats and in a position to help - extensive networking, an immigrant herself, former teacher, community leader, TV talk show host, author, mother, grandmother, etc.

Industry/Entity Type

Business

Coding

Coded - Design and coding required

Number of Pages Required

5+ page

Font styles to use
Sans Serif

Colors
cadf82
add136

Requirements
Must have
• visuals of Marla - present image of competency, caring, professionalism; need to include a 30-second video (in process of being produced) of Marla promoting the services, need to include 5-6 testimonials (which will be sent later). Please see the document that describes the different pages of the website and what should be included. Give the image of Marla's ability to help people GROW into a more productive self
Nice to have
• This is a sole proprietor business and as such, need to have people feel comfortable in who I am - trust is critical and that is why experience and competency should be shown

```html
<!DOCTYPE html>
<html lang="en">
<head>
<meta charset="utf-8">
<title>The Pell R Group – Creating Better Tomorrows</title>
<link href="https://fonts.googleapis.com/css2?family=Open+Sans:ital,wght@0,400;0,600;0,700;0,800;1,400&family=Sorts+Mill+Goudy&display=swap" rel="stylesheet">
<style>
:root{
  --green:#8dc63f;
  --green-soft:#cadf82;
  --green-band:#9fcb54;
  --ink:#1c1c1c;
  --muted:#555;
  --grey:#8a8a8a;
  --offwhite:#f6f8f1;
  --black:#050505;
}
*{margin:0;padding:0;box-sizing:border-box}
html,body{width:947px;height:1200px;overflow:hidden;background:#fff}
body{position:relative;font-family:"Open Sans",sans-serif;color:var(--ink)}
.abs{position:absolute}
.serif{font-family:"Sorts Mill Goudy",serif}

/* header */
.brand{left:66px;top:22px;width:150px;text-align:center}
.brand-mark{width:54px;height:54px;border:3px solid var(--green);border-radius:50%;margin:0 auto 6px}
.brand-name{font-family:"Sorts Mill Goudy",serif;font-size:17px;color:var(--green);white-space:nowrap}
.call{right:64px;top:12px;display:flex;align-items:center;gap:10px;font-size:15px;color:var(--grey)}
.call-icon{width:33px;height:33px;border:1.5px solid var(--green);border-radius:50%;display:flex;align-items:center;justify-content:center}
.call b{color:var(--green);font-size:20px;font-weight:700}
.nav{right:64px;top:63px;display:flex;gap:30px;font-size:13.5px;color:var(--grey)}
.nav span{display:flex;align-items:center;gap:5px}
.nav i{width:17px;height:17px;border:1.3px solid #c9c9c9;border-radius:50%;display:inline-block}
.nav .active{color:var(--green)}
.nav .active i{border-color:var(--green)}

/* hero */
.hero{left:0;top:99px;width:947px;height:560px;background:linear-gradient(180deg,#8a8784 0%,#6f6158 40%,#5d4738 65%,#6b5644 100%)}
.hero-copy{left:0;top:190px;width:947px;text-align:center;color:#fff}
.hero-copy h1{font-size:41px;font-weight:800;letter-spacing:-1px;text-shadow:0 2px 4px rgba(0,0,0,.5)}
.hero-copy p{font-size:15px;margin-top:12px}
.btn{display:inline-block;background:#fff;border:3px solid var(--green-soft);border-radius:24px;color:var(--ink);font-size:14.5px}
.hero-btn{left:384px;top:287px;width:179px;height:40px;line-height:34px;text-align:center}
.waves{left:0;top:0}

/* services */
.svc{width:114px;height:114px;border-radius:50%;background:#fff;box-shadow:0 0 6px rgba(0,0,0,.08);display:flex;align-items:center;justify-content:center}
.svc-in{width:98px;height:98px;border-radius:50%;border:3px solid var(--green-soft);background:radial-gradient(#fff 55%,#eef4e2);display:flex;align-items:center;justify-content:center}
.svc-in.on{background:var(--green);border-color:var(--green)}
.svc-label{width:170px;text-align:center;font-family:"Sorts Mill Goudy",serif;font-size:15.5px;line-height:16px;color:var(--green)}
.svc-label.on{color:var(--ink)}

/* about */
.profile{left:590px;top:612px;width:200px;text-align:center}
.profile h3{font-family:"Sorts Mill Goudy",serif;font-weight:400;font-size:21px}
.profile p{color:var(--green);font-size:15px}
.frame{left:575px;top:672px;width:230px;height:231px;background:#fff;box-shadow:3px 4px 8px rgba(0,0,0,.18)}
.portrait{left:584px;top:681px;width:213px;height:213px;background:linear-gradient(160deg,#4a4a4e,#6b5a55 55%,#8a7066)}
.about-title{left:62px;top:706px;font-family:"Sorts Mill Goudy",serif;font-size:31px;font-weight:400}
.about-title em{font-style:normal;color:var(--green)}
.about-text{left:62px;top:756px;width:455px;font-size:11.6px;line-height:18px;color:var(--muted)}
.learn{left:62px;top:845px;width:145px;height:40px;line-height:34px;text-align:center}

/* footer */
.footer{left:0;top:944px;width:947px;height:197px;background:var(--green-band)}
.col{top:968px}
.col h4{font-family:"Sorts Mill Goudy",serif;font-weight:400;font-size:16px;color:var(--ink);margin-bottom:11px}
.links li{list-style:none;font-size:11.6px;line-height:24.6px;color:#222}
.links li::before{content:"›";margin-right:8px}
.contact-row{display:flex;gap:10px;align-items:flex-start;margin-bottom:12px;font-size:12.5px;color:#222;line-height:17px}
.contact-row.faint{color:#dfeec4;font-size:11.5px}
.news{display:flex;gap:10px;margin-bottom:16px}
.thumb{width:41px;height:41px;flex:none}
.news p{font-size:11.5px;line-height:13.5px;color:#eaf4d6}
.news small{display:block;font-size:9px;color:#dcebbf;margin-top:5px}
.arrows{left:848px;top:971px;display:flex;gap:3px}
.arrows span{width:17px;height:17px;border:1px solid #222;display:flex;align-items:center;justify-content:center;font-size:11px}
.arrows span.dark{background:#111;color:#fff}
.avatar{left:689px;top:1001px;width:50px;height:50px;border-radius:50%;background:linear-gradient(#d7d2cb,#6d6a6a);border:2px solid #fff}
.t-name{left:748px;top:1004px;font-family:"Sorts Mill Goudy",serif;font-size:15.5px}
.t-role{left:749px;top:1024px;font-size:11px;font-style:italic;color:#fff}
.t-quote{left:690px;top:1040px;width:205px;font-size:9.6px;line-height:16.4px;color:#edf5de;text-indent:58px}
.t-more{left:812px;top:1103px;font-size:13px;font-weight:700;text-decoration:underline;color:#333}
.bottom{left:0;top:1141px;width:947px;height:59px;background:var(--black);color:#fff;text-align:center;line-height:59px;font-size:12px}
.bottom b{font-family:"Sorts Mill Goudy",serif;font-weight:400;color:var(--green);font-size:15px}
</style>
</head>
<body>

<header>
  <div class="abs brand">
    <div class="brand-mark"></div>
    <div class="brand-name">The Pell R Group</div>
  </div>
  <div class="abs call">
    <span class="call-icon"><svg width="14" height="14" viewBox="0 0 24 24"><path d="M6.6 10.8a15 15 0 0 0 6.6 6.6l2.2-2.2c.3-.3.7-.4 1-.2 1.1.4 2.3.6 3.6.6.6 0 1 .4 1 1V20c0 .6-.4 1-1 1A17 17 0 0 1 3 4c0-.6.4-1 1-1h3.5c.6 0 1 .4 1 1 0 1.2.2 2.4.6 3.6.1.3 0 .7-.2 1z" fill="none" stroke="#8dc63f" stroke-width="1.5"/></svg></span>
    CONTACT US NOW : <b>(410) 555-0148</b>
  </div>
  <nav class="abs nav">
    <span class="active"><i></i>Home</span>
    <span><i></i>Bio</span>
    <span><i></i>Services</span>
    <span><i></i>Book</span>
    <span><i></i>Media</span>
    <span><i></i>Contact Us</span>
  </nav>
</header>

<section>
  <div class="abs hero" role="img" aria-label="Photo of young people jumping joyfully on a beach at sunset"></div>
  <svg class="abs waves" width="947" height="720" viewBox="0 0 947 720">
    <path d="M0 481 C80 515 140 545 210 543 C330 540 430 500 540 470 C620 448 660 425 700 420 C780 410 870 405 947 403 L947 720 L0 720 Z" fill="#fff"/>
    <path d="M0 481 C80 515 140 545 210 543 C330 540 430 500 540 470 C620 448 660 425 700 420 C780 410 870 405 947 403 L947 560 C820 580 700 620 560 655 C420 680 280 680 160 650 C90 632 40 615 0 605 Z" fill="#f6f8f1"/>
    <path d="M0 481 C80 515 140 545 210 543 C330 540 430 500 540 470 C620 448 660 425 700 420 C780 410 870 405 947 403" fill="none" stroke="#8dc63f" stroke-width="3"/>
  </svg>
  <div class="abs hero-copy">
    <h1>CREATING BETTER TOMORROWS</h1>
    <p>Are you an immigrant needing help navigating the American system?</p>
  </div>
  <a class="abs btn hero-btn">CONTACT US NOW</a>
</section>

<section>
  <div class="abs svc" style="left:86px;top:473px"><div class="svc-in on">
    <svg width="56" height="56" viewBox="0 0 56 56" fill="none" stroke="#111" stroke-width="4"><circle cx="28" cy="12" r="5" fill="#111"/><circle cx="10" cy="42" r="5" fill="#111"/><circle cx="46" cy="42" r="5" fill="#111"/><path d="M20 22c-8 2-10 12-4 16M36 22c8 2 10 12 4 16M18 46c6 4 14 4 20 0M22 24c0 8 12 8 12 0"/></svg>
  </div></div>
  <div class="abs svc-label on" style="left:58px;top:596px">Life coaching</div>

  <div class="abs svc" style="left:250px;top:473px"><div class="svc-in">
    <svg width="44" height="54" viewBox="0 0 44 54"><rect x="3" y="6" width="38" height="46" fill="none" stroke="#555" stroke-width="4"/><rect x="14" y="2" width="16" height="8" fill="#555"/><path d="M10 22l4 4 6-8M10 38l4 4 6-8" fill="none" stroke="#555" stroke-width="2.5"/><path d="M24 22h12M24 26h10M24 38h12M24 42h10" stroke="#555" stroke-width="2.5"/></svg>
  </div></div>
  <div class="abs svc-label" style="left:222px;top:596px">Acculturation</div>

  <div class="abs svc" style="left:415px;top:424px"><div class="svc-in">
    <svg width="66" height="50" viewBox="0 0 66 50" fill="#555" stroke="#555"><circle cx="33" cy="5" r="4"/><rect x="29" y="11" width="8" height="14" rx="2"/><circle cx="8" cy="22" r="4"/><rect x="4" y="28" width="8" height="16" rx="2"/><circle cx="58" cy="22" r="4"/><rect x="54" y="28" width="8" height="16" rx="2"/><circle cx="20" cy="14" r="3"/><circle cx="46" cy="14" r="3"/><path d="M12 36L33 28L54 36" fill="none" stroke-width="1.5"/></svg>
  </div></div>
  <div class="abs svc-label" style="left:387px;top:548px">Intergenerational<br>Relations</div>

  <div class="abs svc" style="left:579px;top:366px"><div class="svc-in">
    <svg width="56" height="50" viewBox="0 0 56 50" fill="#555"><circle cx="28" cy="6" r="5"/><rect x="22" y="13" width="12" height="36" rx="3"/><circle cx="14" cy="12" r="4"/><rect x="9" y="18" width="10" height="31" rx="3"/><circle cx="42" cy="12" r="4"/><rect x="37" y="18" width="10" height="31" rx="3"/><rect x="1" y="24" width="8" height="25" rx="3"/><rect x="47" y="24" width="8" height="25" rx="3"/></svg>
  </div></div>
  <div class="abs svc-label" style="left:551px;top:491px">Leadership<br>development</div>

  <div class="abs svc" style="left:744px;top:383px"><div class="svc-in">
    <svg width="50" height="50" viewBox="0 0 50 50" fill="#555"><circle cx="25" cy="8" r="6"/><path d="M15 24c0-6 20-6 20 0v2H15z"/><path d="M8 38V32h34v6M25 28v10" fill="none" stroke="#555" stroke-width="3"/><circle cx="8" cy="41" r="4"/><circle cx="25" cy="41" r="4"/><circle cx="42" cy="41" r="4"/></svg>
  </div></div>
  <div class="abs svc-label" style="left:716px;top:507px">Organizational<br>management</div>
</section>

<section>
  <div class="abs profile">
    <h3>Marla Fenwick</h3>
    <p>California</p>
  </div>
  <div class="abs frame"></div>
  <div class="abs portrait" role="img" aria-label="Portrait photo of Marla Fenwick"></div>

  <h2 class="abs about-title">About <em>The Pell R Group</em></h2>
  <p class="abs about-text">Life coach (this is a business that is focused on the individual – Marla Fenwick.As such, need to present Marla as a mature professional with extensive experience in working with people and someone who has been very effective in getting things done.</p>
  <a class="abs btn learn">LEARN MORE</a>
</section>

<footer>
  <div class="abs footer"></div>

  <div class="abs col" style="left:62px">
    <h4>Useful Links</h4>
    <ul class="links"><li>Home</li><li>About</li><li>Services</li><li>Book</li><li>Contact Us</li></ul>
  </div>

  <div class="abs col" style="left:271px;width:200px">
    <h4>Contact Info</h4>
    <div class="contact-row"><svg width="14" height="20" viewBox="0 0 14 20"><path d="M7 0a7 7 0 0 0-7 7c0 5 7 13 7 13s7-8 7-13a7 7 0 0 0-7-7z" fill="#222"/><circle cx="7" cy="7" r="2.5" fill="#9fcb54"/></svg><span>2716 Quiet Willow Lane,<br>Laurel, MD 20707</span></div>
    <div class="contact-row faint"><svg width="15" height="15" viewBox="0 0 24 24"><path d="M6.6 10.8a15 15 0 0 0 6.6 6.6l2.2-2.2c.3-.3.7-.4 1-.2 1.1.4 2.3.6 3.6.6.6 0 1 .4 1 1V20c0 .6-.4 1-1 1A17 17 0 0 1 3 4c0-.6.4-1 1-1h3.5c.6 0 1 .4 1 1 0 1.2.2 2.4.6 3.6.1.3 0 .7-.2 1z" fill="#222"/></svg><span>(410) 555-0148</span></div>
    <div class="contact-row faint"><svg width="15" height="12" viewBox="0 0 15 12"><rect x=".5" y=".5" width="14" height="11" fill="none" stroke="#222"/><path d="M.5.5l7 6 7-6M.5 11.5l5-5M14.5 11.5l-5-5" fill="none" stroke="#222"/></svg><span>info@thepellrgroup.com</span></div>
  </div>

  <div class="abs col" style="left:480px;width:185px">
    <h4>Latest News</h4>
    <div class="news"><div class="thumb" role="img" aria-label="News photo of two people at a table" style="background:linear-gradient(#8a5a2e,#c79a5a)"></div><div><p>Lorem Ipsum is simply dummy text of</p><small>12.06.2014</small></div></div>
    <div class="news"><div class="thumb" role="img" aria-label="News photo of a woman reading" style="background:linear-gradient(#e8e4df,#b5473a)"></div><div><p>Lorem Ipsum is simply dummy text of</p><small>12.06.2014</small></div></div>
  </div>

  <div class="abs col" style="left:689px"><h4>Testimonials</h4></div>
  <div class="abs arrows"><span>‹</span><span class="dark">›</span></div>
  <div class="abs avatar" role="img" aria-label="Photo of testimonial author"></div>
  <div class="abs t-name">DANA K</div>
  <div class="abs t-role">CEO</div>
  <p class="abs t-quote">"Our Family Was In A Crisis Situation Dealing With The Addictiion Of Our Son. Marla Was A Tremendous Source Of Support And Comfort During Our Time Of Desperate Need...</p>
  <a class="abs t-more">READ MORE</a>

  <div class="abs bottom">© <b>THE PELL R GROUP</b> - 2017. All Rights Reserved.</div>
</footer>

</body>
</html>
```